Software as a Service to manage Home Care Management

We need a web site designed for Home Care Management Software as a Service product, that facilitates Home Care organizations to manage and schedule carers to visit client homes. We want a modern look and feel using our existing logo.

Target Market(s)

Home Care Management organizations. Product is similar to: https://kelvantro.co/

Coding

Coded - Design and coding required

Number of Pages Required

3 page

```html
<!DOCTYPE html>
<html lang="en">
<head>
<meta charset="utf-8">
<title>Hearthline — Home Care Management</title>
<link href="https://fonts.googleapis.com/css2?family=Poppins:wght@300;400;500;600;700&display=swap" rel="stylesheet">
<style>
:root{
  --purple:#7a4fd8;
  --magenta:#d43aa6;
  --violet-deep:#4b2a8c;
  --ink:#1f1b2d;
  --text:#6f6b7a;
  --muted:#a9a6b3;
  --soft:#c89ae0;
  --line:#ece9f1;
  --foot:#efeff2;
  --teal:#43c6c0;
  --orange:#ff6a2a;
  --green:#2fbf6a;
  --red:#e0384a;
  --board-top:#f4f4f5;
  --board-bottom:#cfcfd3;
}
*{box-sizing:border-box;margin:0;padding:0}
html,body{width:1200px;height:2219px;overflow:hidden}
body{font-family:"Poppins",sans-serif;color:var(--ink);background:linear-gradient(180deg,var(--board-top),var(--board-bottom));position:relative}
.page{position:absolute;background:#fff;overflow:hidden;box-shadow:0 6px 22px rgba(40,30,70,.14)}
.abs{position:absolute}
.brand{position:absolute;display:flex;align-items:center;gap:3px;font-size:7px;font-weight:600;color:var(--ink);letter-spacing:.2px;white-space:nowrap;line-height:1}
.brand i{display:block;width:7px;height:7px;border-radius:50%;background:var(--magenta)}
.nav{position:absolute;display:flex;gap:7px;font-size:4.2px;font-weight:500;color:#fff;line-height:1}
.signin{position:absolute;font-size:4px;line-height:1;font-weight:600;color:#fff;background:var(--magenta);border-radius:6px;padding:2px 6px;box-shadow:0 1px 3px rgba(212,58,166,.5)}
.hero-title{position:absolute;font-size:11.5px;font-weight:600;line-height:1.5;color:var(--ink);white-space:nowrap}
.hero-sub{position:absolute;font-size:5.6px;line-height:1.2;color:var(--text);white-space:nowrap}
.btn{position:absolute;font-size:4px;line-height:1;font-weight:500;border-radius:8px;padding:3px 9px;white-space:nowrap}
.btn-fill{color:#fff;background:linear-gradient(90deg,var(--purple),var(--magenta));box-shadow:0 2px 4px rgba(122,79,216,.35)}
.btn-line{color:var(--ink);border:1px solid var(--magenta);background:#fff}
.stat{position:absolute;font-size:14px;line-height:1;font-weight:300;color:var(--soft);white-space:nowrap}
.stat small{font-size:4.3px;font-weight:500;color:var(--ink)}
.center{position:absolute;left:0;right:0;text-align:center}
.h2{font-size:8.6px;line-height:1.2;font-weight:600;color:var(--ink)}
.p{font-size:4.2px;line-height:1.75;color:var(--text)}
.feat{position:absolute;width:100px;text-align:center;font-size:3.8px;line-height:1.5}
.feat svg{display:block;margin:0 auto 3px}
.feat b{display:block;font-size:5px;line-height:1.3;font-weight:500;color:var(--ink);margin-bottom:3px}
.feat span{display:block;font-size:3.8px;line-height:1.5;color:var(--text)}
.chev{position:absolute;width:8px;height:8px;border-radius:50%;background:#f0eef3;font-size:5px;line-height:8px;text-align:center;color:var(--text)}
.underline{position:absolute;height:1.5px;background:linear-gradient(90deg,var(--purple),var(--magenta))}
.art{position:absolute}
.section-title{position:absolute;font-size:8.8px;font-weight:600;line-height:1.45;white-space:nowrap}
.discover{position:absolute;font-size:4px;line-height:1;font-weight:600;color:var(--purple)}
.tl-item{position:absolute;left:307px;width:100px;font-size:3.8px;line-height:1.55}
.tl-item b{display:block;font-size:4.6px;line-height:1.3;font-weight:500;margin-bottom:2px}
.tl-item span{display:block;font-size:3.8px;line-height:1.55;color:var(--text)}
.tl-dot{position:absolute;width:18px;height:18px;border-radius:50%;background:#fff;border:1px solid var(--line);box-shadow:0 1px 4px rgba(122,79,216,.2)}
.tl-dot.on{border-color:var(--purple)}
.tile{position:absolute;border-radius:6px;background:#edeaf7}
.footer-arc{position:absolute;left:0;width:100%}
.fcol{position:absolute;font-size:3.7px;line-height:1.7;color:var(--text)}
.fcol b{display:block;font-size:4.2px;font-weight:600;color:var(--ink);margin-bottom:3px}
.social{position:absolute;display:flex;gap:5px}
.social i{display:block;width:5px;height:5px;border-radius:50%;background:#8f8b99}
.copy{position:absolute;font-size:3.6px;line-height:1.2;color:var(--text)}
.copy u{text-decoration:underline}
.rule{position:absolute;height:1px;background:#dcdae2}
.dots{position:absolute;display:flex;gap:3px}
.dots i{display:block;width:6px;height:6px;border-radius:50%;background:var(--purple)}
.card{position:absolute;border:1px solid #e2dfe8;border-radius:4px;background:#fff;text-align:center;font-size:4px;line-height:1.3}
.card.pick{border:1.5px solid var(--magenta);box-shadow:0 3px 10px rgba(212,58,166,.18)}
.card b{display:block;font-size:6px;font-weight:600;margin-top:15px}
.card .price{display:block;font-size:13px;line-height:1.2;font-weight:300;color:var(--soft);margin-top:2px}
.card .acc{display:block;font-size:4.2px;color:var(--text);margin-top:2px}
.card ul{list-style:none;font-size:3.5px;line-height:1.55;color:var(--ink);margin-top:9px}
.card li::before{content:"\2713 ";color:var(--green);font-weight:700}
.card li.no::before{content:"\2715 ";color:var(--red)}
.card .go{display:inline-block;margin-top:9px;font-size:3.8px;line-height:1;font-weight:600;padding:3px 14px;border-radius:8px;border:1px solid var(--magenta);color:var(--ink)}
.card.pick .go{background:linear-gradient(90deg,var(--purple),var(--magenta));color:#fff;border:0}
.office{position:absolute;width:100px;height:30px;border:1px solid #e7e5ec;border-radius:3px;background:#fff;display:flex;align-items:center;gap:4px;padding-left:8px;line-height:1.4}
.office b{display:block;font-size:4.6px;font-weight:600}
.office span{display:block;font-size:3.4px;color:var(--text)}
.deco{position:absolute;font-size:7px;line-height:1;color:var(--teal);font-weight:700}
</style>
</head>
<body>

<!-- ================= LONG HOME PAGE ================= -->
<section class="page" style="left:42px;top:53px;width:481px;height:2114px">

  <svg class="art" style="left:216px;top:0" width="265" height="253" viewBox="0 0 265 253" role="img" aria-label="Photo of a smiling carer with an elderly woman holding a cane">
    <defs><linearGradient id="heroA" x1="0" y1="0" x2="1" y2="1"><stop offset="0" stop-color="#7a4fd8"/><stop offset="1" stop-color="#d43aa6"/></linearGradient></defs>
    <path d="M40 0H265V228C205 262 110 258 55 205C5 150 0 60 40 0Z" fill="url(#heroA)"/>
  </svg>

  <div class="brand" style="left:72px;top:25px"><i></i>Hearthline</div>
  <nav class="nav" style="left:282px;top:27px"><span>Home</span><span>Features</span><span>FAQ</span><span>Contact Us</span></nav>
  <span class="signin" style="left:391px;top:25px">Sign In</span>

  <span class="deco" style="left:20px;top:102px">&#10006;</span>
  <h1 class="hero-title" style="left:69px;top:98px">Awesome App for Your<br>Modern Lifestyle</h1>
  <p class="hero-sub" style="left:69px;top:150px">Care Software for the Heroes of Homecare</p>
  <span class="btn btn-fill" style="left:69px;top:176px">Download App</span>
  <span class="btn btn-line" style="left:125px;top:176px">Discover More</span>
  <span class="deco" style="left:20px;top:212px;color:#9b98a6;font-size:6px">&#9670;</span>

  <span class="stat" style="left:95px;top:270px">1,265<small>Users</small></span>
  <span class="stat" style="left:172px;top:270px">1,000<small>Download</small></span>
  <span class="stat" style="left:265px;top:270px">508 <small>Likes</small></span>
  <span class="stat" style="left:340px;top:270px">809<small>5 star Rating</small></span>
  <div class="rule" style="left:70px;width:340px;top:310px;background:var(--line)"></div>

  <h2 class="center h2" style="top:332px">Awesome Apps Features</h2>
  <p class="center p" style="top:349px">Your success is our success, and together we can find the best possible ways of<br>supporting care staff and people at home.</p>
  <p class="center p" style="top:370px">We work closely with care companies to have a system that is fit for the purpose<br>of planning, delivering and reporting homecare.</p>

  <span class="chev" style="left:84px;top:433px">&#8249;</span>
  <span class="chev" style="left:395px;top:433px">&#8250;</span>
  <div class="feat" style="left:84px;top:420px">
    <svg width="12" height="13" viewBox="0 0 12 13"><path d="M6 1a4 4 0 0 1 4 4c0 3-4 7-4 7S2 8 2 5a4 4 0 0 1 4-4z" fill="none" stroke="#6f6b7a" stroke-width="1"/><circle cx="6" cy="5" r="1.4" fill="#6f6b7a"/></svg>
    <b>For Managers</b><span>Care management tools that save your time and money. Enables you to grow your business.</span>
  </div>
  <div class="feat" style="left:188px;top:420px">
    <svg width="13" height="13" viewBox="0 0 13 13"><circle cx="5" cy="4" r="2.6" fill="none" stroke="#7a4fd8"/><path d="M1 12c0-3 2-5 4-5s4 2 4 5" fill="none" stroke="#7a4fd8"/><circle cx="10" cy="10" r="2" fill="none" stroke="#d43aa6"/></svg>
    <b>For Carers</b><span>Simple and easy to use App. Rosters and care plans on the go. More time for care.</span>
  </div>
  <div class="feat" style="left:294px;top:420px">
    <svg width="13" height="13" viewBox="0 0 13 13"><circle cx="7" cy="4" r="2.6" fill="none" stroke="#6f6b7a"/><path d="M2 12c0-3 2-5 5-5s4 2 4 5" fill="none" stroke="#6f6b7a"/></svg>
    <b>For Clients and Families</b><span>Latest information in real time, all documents in one place. Transparency for all.</span>
  </div>
  <div class="underline" style="left:194px;width:90px;top:479px"></div>

  <!-- all-in-one -->
  <div class="art" style="left:60px;top:516px;width:200px;height:212px;border-radius:50%;background:radial-gradient(circle,rgba(212,58,166,.12) 0,rgba(212,58,166,.05) 55%,transparent 70%)"></div>
  <div class="art" role="img" aria-label="Phone showing a visit details screen for a client" style="left:114px;top:520px;width:90px;height:190px;border-radius:14px;background:linear-gradient(180deg,#f7f7f9 0,#f7f7f9 8%,#6a6be0 8%,#7c8ff0 30%,#ffffff 30%,#ffffff 80%,#43c6c0 80%,#43c6c0 88%,#f7f7f9 88%);box-shadow:0 4px 14px rgba(0,0,0,.15)"></div>
  <h3 class="abs" style="left:270px;top:517px;font-size:8px;line-height:1.2;font-weight:600">The All-in-One system</h3>
  <div class="abs" style="left:285px;top:553px;width:1px;height:174px;background:#d9d6e0"></div>
  <span class="tl-dot on" style="left:276px;top:570px"></span>
  <span class="tl-dot" style="left:276px;top:637px"></span>
  <span class="tl-dot" style="left:276px;top:690px"></span>
  <div class="tl-item" style="top:550px"><b>Managers</b><span>All the care management tools you need in one place<br>Rostering, care plans, timesheets, eMAR, reports...<br>World class data protection &amp; compliance<br>In-app support, webinar and training resources for free</span></div>
  <div class="tl-item" style="top:627px"><b>Clients And Family</b><span>Real-time roster and care plans in mobile<br>Simple check-in and out system<br>Risk assessments to keep you safe<br>Paperless reporting tools</span></div>
  <div class="tl-item" style="top:683px"><b>Carers</b><span>Private and unique login area<br>Real time updates and live statuses<br>Manage changes, notes and feedback</span></div>

  <!-- easy to manage -->
  <svg class="abs" style="left:84px;top:798px" width="12" height="12" viewBox="0 0 12 12"><path d="M1 11L11 1M1 1l10 10" stroke="#7a4fd8" stroke-width="1.2"/></svg>
  <h3 class="section-title" style="left:83px;top:818px">Easy to Manage Your All Data<br>by This App</h3>
  <p class="abs p" style="left:83px;top:852px;width:140px;font-size:3.9px">In order to design a mobile app that is going to be module downloaded and accessed frequently by users, you need offer an experience that isn't available elsewhere. Often businesses get caught up.</p>
  <span class="discover" style="left:83px;top:890px">Discover &#8250;</span>
  <div class="art" role="img" aria-label="Dashboard screen with a line chart and user list" style="left:248px;top:780px;width:145px;height:124px;background:linear-gradient(90deg,#9a62e0 0,#9a62e0 6%,#f6f5f9 6%);box-shadow:0 3px 10px rgba(0,0,0,.1)">
    <svg class="abs" style="left:22px;top:30px" width="80" height="40" viewBox="0 0 80 40"><polyline points="0,30 8,12 16,32 24,8 32,28 40,10 48,30 56,14 64,26 72,16 80,24" fill="none" stroke="#7a4fd8" stroke-width="1"/></svg>
  </div>

  <!-- responsive -->
  <div class="art" role="img" aria-label="Stacked phone screens showing the app interface" style="left:91px;top:949px;width:147px;height:123px;border-radius:12px;background:linear-gradient(135deg,#f8f8fb,#e6e3f0);transform:skewY(-8deg);box-shadow:0 6px 14px rgba(0,0,0,.1)"></div>
  <svg class="abs" style="left:248px;top:966px" width="13" height="10" viewBox="0 0 13 10"><rect x=".5" y=".5" width="12" height="7" fill="none" stroke="#7a4fd8"/><path d="M4 9.5h5" stroke="#7a4fd8"/></svg>
  <h3 class="section-title" style="left:248px;top:986px">Responsive Design for All<br>Devices with Quality</h3>
  <p class="abs p" style="left:248px;top:1019px;width:150px;font-size:3.9px">In order to design a mobile app that is going to be module downloaded and accessed frequently by users, you need offer an experience that isn't available elsewhere. Often businesses get caught up.</p>
  <span class="discover" style="left:248px;top:1058px">Discover &#8250;</span>

  <!-- tutorial band -->
  <div class="art" role="img" aria-label="Photo of hands typing on a laptop with a purple overlay" style="left:0;top:1112px;width:481px;height:132px;background:linear-gradient(120deg,#5a3aa0,#3e2578 60%,#6c4bb0)"></div>
  <h3 class="center" style="top:1147px;font-size:8.5px;line-height:1.2;font-weight:600;color:#fff">Watch a Quick Tutorial</h3>
  <div class="abs" style="left:229px;top:1179px;width:24px;height:24px;border-radius:50%;background:linear-gradient(135deg,#d43aa6,#e8487a);box-shadow:0 0 0 4px rgba(255,255,255,.15)">
    <svg width="24" height="24" viewBox="0 0 24 24"><path d="M10 8l6 4-6 4z" fill="#fff"/></svg>
  </div>

  <!-- screenshots -->
  <h2 class="center h2" style="top:1285px">App ScreenShots</h2>
  <p class="center p" style="top:1305px">A Private Limited is the most popular type of partnership Malta. The limited liability<br>is, in fact, the only type of company allowed by Companies.</p>
  <div class="art" role="img" aria-label="Fan of app screenshots: contacts list, calendar, booking detail and profile" style="left:83px;top:1345px;width:323px;height:180px;background:linear-gradient(90deg,#f4f4f7 0,#ffffff 18%,#f8f8fb 30%,#ffffff 42%,#eae7f5 62%,#5a6490 64%,#5a6490 80%,#ffffff 82%,#f4f4f7 100%);box-shadow:0 4px 12px rgba(0,0,0,.08)"></div>
  <span class="chev" style="left:230px;top:1540px;background:#fff;border:1px solid var(--line)">&#8249;</span>
  <span class="chev" style="left:249px;top:1540px;background:#fff;border:1px solid var(--line)">&#8250;</span>

  <!-- integrations -->
  <h3 class="section-title" style="left:83px;top:1613px">Designed &amp; Worked<br>by the Latest Integration</h3>
  <p class="abs p" style="left:83px;top:1647px;width:130px;font-size:3.9px">A Private Limited is the most popular type of partnership Malta. The limited liability is, in fact, the only type of the company allowed by Companies.</p>
  <span class="discover" style="left:83px;top:1676px">Discover &#8250;</span>
  <span class="tile" style="left:302px;top:1593px;width:47px;height:47px"></span>
  <span class="tile" style="left:355px;top:1606px;width:32px;height:32px;background:#fbe9e4"></span>
  <span class="tile" style="left:272px;top:1644px;width:30px;height:26px;background:#f3f1f8"></span>
  <span class="tile" style="left:310px;top:1649px;width:35px;height:40px;background:#e6effa"></span>
  <span class="tile" style="left:353px;top:1646px;width:53px;height:53px;background:#e9eaf2"></span>

  <!-- testimonial -->
  <h3 class="section-title" style="left:230px;top:1744px">Some Talk of Our<br>Honorable Clients</h3>
  <div class="art" role="img" aria-label="Portrait photo of a smiling client" style="left:108px;top:1787px;width:82px;height:86px;border-radius:50%;background:radial-gradient(circle at 50% 40%,#e8c8b2,#c89a80 60%,#f6e6f2 62%)"></div>
  <div class="art" role="img" aria-label="Small client portrait" style="left:84px;top:1845px;width:20px;height:20px;background:#e6d3c6"></div>
  <div class="art" role="img" aria-label="Small client portrait" style="left:145px;top:1875px;width:12px;height:10px;background:#d8c4b8"></div>
  <div class="art" role="img" aria-label="Small client portrait" style="left:189px;top:1871px;width:16px;height:14px;background:#d8c4b8"></div>
  <p class="abs" style="left:211px;top:1778px;font-size:4px;line-height:1.2;color:var(--text)">&#9633; Marla Quinn</p>
  <p class="abs p" style="left:211px;top:1793px;width:190px;font-size:4.2px">The number of ICOs being launched is increasing every day. The right team can help your ICO stand out from the crowd. We're that team.</p>
  <p class="abs" style="left:211px;top:1815px;font-size:5px;line-height:1.2;font-weight:500">Marla Quinn</p>
  <p class="abs" style="left:211px;top:1826px;font-size:3.6px;line-height:1.2;color:var(--purple)">CEO</p>
  <span class="abs" style="left:235px;top:1878px;font-size:7px;line-height:1;color:var(--violet-deep)">&#8592; &#8594;</span>

  <!-- newsletter -->
  <h3 class="abs" style="left:71px;top:1917px;font-size:10.5px;line-height:1.2;font-weight:700;color:var(--violet-deep);letter-spacing:.3px">NEWSLETTER</h3>
  <p class="abs" style="left:71px;top:1932px;font-size:4px;line-height:1.2;color:var(--text)">Please Enter your Email Address and Get New Updates.</p>
  <div class="art" role="img" aria-label="Decorative paper plane flying along a dotted trail" style="left:35px;top:1942px;width:42px;height:28px;border-radius:6px;background:linear-gradient(135deg,#f1ecfa,#fde6da)"></div>
  <div class="abs" style="left:249px;top:1917px;width:170px;height:16px;border-radius:9px;background:#fff;box-shadow:0 2px 6px rgba(0,0,0,.08);font-size:4px;color:var(--text);line-height:16px;padding-left:9px">Enter your email address</div>
  <span class="abs" style="left:370px;top:1917px;width:47px;height:16px;border-radius:9px;background:var(--orange);font-size:3.8px;font-weight:600;color:#fff;text-align:center;line-height:16px">SUBSCRIBE</span>

  <!-- footer -->
  <svg class="footer-arc" style="top:1995px" width="481" height="119" viewBox="0 0 481 119" preserveAspectRatio="none"><path d="M0 40Q240 -20 481 40V119H0Z" fill="#efeff2"/></svg>
  <div class="brand" style="left:71px;top:2006px"><i></i>Hearthline</div>
  <p class="fcol" style="left:71px;top:2024px;width:85px;color:var(--ink)">Be the first to find out about exclusive deals, the latest Lookbooks trends. We're on a mission to build a better future where technology.</p>
  <div class="social" style="left:71px;top:2061px"><i></i><i></i><i></i><i></i></div>
  <div class="fcol" style="left:159px;top:2005px"><b>Address</b>Phone: &nbsp;+1 555 014 2290<br>Email: &nbsp;hello@hearthline.co<br>Address: &nbsp;Maple Hollow, Ridgefield,<br>United States</div>
  <div class="fcol" style="left:248px;top:2005px"><b>Quick Links</b>Privacy Policy &nbsp; About Us<br>Contact Us</div>
  <div class="fcol" style="left:337px;top:2005px;width:85px"><b>Twitter</b>&#9679; Lorem ipsum dolor sit amet, con sectetur adipiscing elit, sed do eius mod tempor incididunt. 3<br>@hearthline</div>
  <div class="dots" style="left:337px;top:2056px"><i></i><i></i></div>
  <div class="rule" style="left:71px;width:345px;top:2089px"></div>
  <p class="copy" style="left:71px;top:2099px">&copy; 2020, Hearthline | <u>Privacy Policy</u> | <u>Site Map</u></p>
  <p class="copy" style="left:382px;top:2099px">All Right Reserved</p>
  <span class="deco" style="left:432px;top:2093px">&#10006;</span>
</section>

<!-- ================= HOME HERO (desktop view) ================= -->
<section class="page" style="left:606px;top:125px;width:511px;height:284px">
  <svg class="art" style="left:220px;top:0" width="291" height="233" viewBox="0 0 265 253" preserveAspectRatio="none" role="img" aria-label="Photo of a smiling carer with an elderly woman holding a cane">
    <path d="M40 0H265V228C205 262 110 258 55 205C5 150 0 60 40 0Z" fill="url(#heroA)"/>
  </svg>
  <div class="brand" style="left:84px;top:14px"><i></i>Hearthline</div>
  <nav class="nav" style="left:284px;top:17px"><span>Home</span><span>Features</span><span>FAQ</span><span>Contact Us</span></nav>
  <span class="signin" style="left:390px;top:15px">Sign In</span>
  <span class="deco" style="left:33px;top:90px">&#10006;</span>
  <h1 class="hero-title" style="left:79px;top:86px">Awesome App for Your<br>Modern Lifestyle</h1>
  <p class="hero-sub" style="left:79px;top:134px">Care Software for the Heroes of Homecare</p>
  <span class="btn btn-fill" style="left:79px;top:159px">Download App</span>
  <span class="btn btn-line" style="left:135px;top:159px">Discover More</span>
  <span class="deco" style="left:33px;top:198px;color:#9b98a6;font-size:6px">&#9670;</span>
  <span class="stat" style="left:104px;top:251px">1,265<small>Users</small></span>
  <span class="stat" style="left:179px;top:251px">1,000<small>Download</small></span>
  <span class="stat" style="left:267px;top:251px">508 <small>Likes</small></span>
  <span class="stat" style="left:340px;top:251px">809<small>5 star Rating</small></span>
</section>

<!-- ================= PRICING PAGE ================= -->
<section class="page" style="left:621px;top:640px;width:480px;height:700px">
  <svg class="art" style="left:210px;top:0" width="270" height="183" viewBox="0 0 265 253" preserveAspectRatio="none" role="img" aria-label="Illustration of stacked phone screens showing the app">
    <path d="M40 0H265V228C205 262 110 258 55 205C5 150 0 60 40 0Z" fill="url(#heroA)"/>
  </svg>
  <div class="brand" style="left:68px;top:25px"><i></i>Hearthline</div>
  <nav class="nav" style="left:278px;top:27px"><span>Home</span><span>Features</span><span>FAQ</span><span>Contact Us</span></nav>
  <span class="signin" style="left:388px;top:25px">Sign In</span>
  <span class="deco" style="left:16px;top:102px">&#10006;</span>
  <h1 class="hero-title" style="left:65px;top:77px">Awesome App for Your<br>Modern Lifestyle</h1>
  <p class="hero-sub" style="left:65px;top:129px">Care Software for the Heroes of Homecare</p>
  <span class="btn btn-fill" style="left:65px;top:156px">Download App</span>
  <span class="btn btn-line" style="left:121px;top:156px">Discover More</span>

  <span class="chev" style="left:79px;top:224px">&#8249;</span>
  <span class="chev" style="left:390px;top:224px">&#8250;</span>
  <div class="feat" style="left:80px;top:210px">
    <svg width="12" height="13" viewBox="0 0 12 13"><path d="M6 1a4 4 0 0 1 4 4c0 3-4 7-4 7S2 8 2 5a4 4 0 0 1 4-4z" fill="none" stroke="#6f6b7a"/><circle cx="6" cy="5" r="1.4" fill="#6f6b7a"/></svg>
    <b>For Managers</b><span>Care management tools that save your time and money. Enables you to grow your business.</span>
  </div>
  <div class="feat" style="left:190px;top:210px">
    <svg width="13" height="13" viewBox="0 0 13 13"><circle cx="5" cy="4" r="2.6" fill="none" stroke="#7a4fd8"/><path d="M1 12c0-3 2-5 4-5s4 2 4 5" fill="none" stroke="#7a4fd8"/><circle cx="10" cy="10" r="2" fill="none" stroke="#d43aa6"/></svg>
    <b>For Carers</b><span>Simple and easy to use App. Rosters and care plans on the go. More time for care.</span>
  </div>
  <div class="feat" style="left:300px;top:210px">
    <svg width="13" height="13" viewBox="0 0 13 13"><circle cx="7" cy="4" r="2.6" fill="none" stroke="#6f6b7a"/><path d="M2 12c0-3 2-5 5-5s4 2 4 5" fill="none" stroke="#6f6b7a"/></svg>
    <b>For Clients and Families</b><span>Latest information in real time, all documents in one place. Transparency for all.</span>
  </div>
  <div class="underline" style="left:190px;width:100px;top:267px"></div>

  <h2 class="center h2" style="top:316px">Get in Reasonable Price</h2>
  <p class="center p" style="top:334px;font-size:4px">A Private Limited is the most popular type of partnership Malta. The limited<br>liability is, in fact, the only type of company allowed by Companies.</p>
  <div class="abs" style="left:210px;top:379px;display:flex;align-items:center;gap:4px;font-size:4.2px;line-height:1">
    <span style="color:var(--text)">Monthly</span>
    <span style="display:block;width:16px;height:8px;border-radius:4px;background:var(--purple);position:relative"><i style="position:absolute;left:1px;top:1px;width:6px;height:6px;border-radius:50%;background:#fff"></i></span>
    <span style="font-weight:600">Yearly</span>
  </div>

  <div class="card" style="left:79px;top:411px;width:101px;height:136px">
    <b>Personal</b><span class="price">$12</span><span class="acc">Limited Access</span>
    <ul><li>100 GB Disk Space</li><li>2 Sub domains</li><li>5 Email Accounts</li><li class="no">No License</li><li class="no">Phone &amp; Mail Support</li></ul>
    <span class="go">Get Started</span>
  </div>
  <div class="card pick" style="left:190px;top:405px;width:101px;height:148px">
    <b style="margin-top:20px">Business</b><span class="price">$23</span><span class="acc">Limited Access</span>
    <ul><li>200 GB Disk Space</li><li>5 Sub domains</li><li>10 Email Accounts</li><li>6 Month License</li><li class="no">Phone &amp; Mail Support</li></ul>
    <span class="go">Get Started</span>
  </div>
  <div class="card" style="left:301px;top:411px;width:101px;height:136px">
    <b>Enterprise</b><span class="price">$39</span><span class="acc">Unlimited Access</span>
    <ul><li>300 GB Disk Space</li><li>15 Sub domains</li><li>15 Email Accounts</li><li>2 Year License</li><li>Phone &amp; Mail Support</li></ul>
    <span class="go">Get Started</span>
  </div>

  <svg class="footer-arc" style="top:580px" width="480" height="120" viewBox="0 0 481 119" preserveAspectRatio="none"><path d="M0 40Q240 -20 481 40V119H0Z" fill="#efeff2"/></svg>
  <div class="brand" style="left:68px;top:591px"><i></i>Hearthline</div>
  <p class="fcol" style="left:67px;top:610px;width:85px;color:var(--ink)">Be the first to find out about exclusive deals, the latest Lookbooks trends. We're on a mission to build a better future where technology.</p>
  <div class="social" style="left:67px;top:646px"><i></i><i></i><i></i><i></i></div>
  <div class="fcol" style="left:155px;top:590px"><b>Address</b>Phone: &nbsp;+1 555 014 2290<br>Email: &nbsp;hello@hearthline.co<br>Address: &nbsp;Maple Hollow, Ridgefield,<br>United States</div>
  <div class="fcol" style="left:244px;top:590px"><b>Quick Links</b>Privacy Policy &nbsp; About Us<br>Contact Us</div>
  <div class="fcol" style="left:333px;top:590px;width:85px"><b>Twitter</b>&#9679; Lorem ipsum dolor sit amet, con sectetur adipiscing elit, sed do eius mod tempor incididunt. 2<br>@hearthline</div>
  <div class="dots" style="left:333px;top:636px"><i></i><i></i></div>
  <p class="copy" style="left:67px;top:684px">&copy; 2020, Hearthline | <u>Privacy Policy</u> | <u>Site Map</u></p>
  <p class="copy" style="left:377px;top:684px">All Right Reserved</p>
  <span class="deco" style="left:426px;top:679px">&#10006;</span>
</section>

<!-- ================= CONTACT PAGE ================= -->
<section class="page" style="left:621px;top:1411px;width:480px;height:625px">
  <svg class="art" style="left:210px;top:0" width="270" height="211" viewBox="0 0 265 253" preserveAspectRatio="none" role="img" aria-label="Photo of a smiling support agent wearing a headset">
    <path d="M40 0H265V228C205 262 110 258 55 205C5 150 0 60 40 0Z" fill="url(#heroA)"/>
  </svg>
  <div class="brand" style="left:69px;top:24px"><i></i>Hearthline</div>
  <nav class="nav" style="left:279px;top:26px"><span>Home</span><span>Features</span><span>FAQ</span><span>Contact Us</span></nav>
  <span class="signin" style="left:389px;top:24px">Sign In</span>
  <span class="deco" style="left:17px;top:100px">&#10006;</span>
  <h1 class="hero-title" style="left:66px;top:76px">Care Software for<br>the Heroes of Homecare</h1>
  <div class="abs" style="left:66px;top:127px;display:flex;gap:4px"><i style="display:block;width:17px;height:8px;border-radius:4px;background:linear-gradient(90deg,var(--purple),var(--magenta))"></i><i style="display:block;width:17px;height:8px;border-radius:4px;border:1px solid var(--magenta)"></i></div>
  <span class="deco" style="left:63px;top:157px;color:#f3d35a">&#10010;</span>

  <h2 class="center h2" style="top:213px;font-size:8px">Contact Us</h2>
  <div class="office" style="left:79px;top:230px"><svg width="10" height="12" viewBox="0 0 12 13"><path d="M6 1a4 4 0 0 1 4 4c0 3-4 7-4 7S2 8 2 5a4 4 0 0 1 4-4z" fill="none" stroke="#3f6fd8"/></svg><div><b>Office address</b><span>14 Lantern Lane, Brookvale</span></div></div>
  <div class="office" style="left:190px;top:230px"><svg width="10" height="12" viewBox="0 0 12 13"><path d="M6 1a4 4 0 0 1 4 4c0 3-4 7-4 7S2 8 2 5a4 4 0 0 1 4-4z" fill="none" stroke="#3f6fd8"/></svg><div><b>Office address</b><span>14 Lantern Lane, Brookvale</span></div></div>
  <div class="office" style="left:300px;top:230px"><svg width="10" height="12" viewBox="0 0 12 13"><path d="M6 1a4 4 0 0 1 4 4c0 3-4 7-4 7S2 8 2 5a4 4 0 0 1 4-4z" fill="none" stroke="#3f6fd8"/></svg><div><b>Office address</b><span>14 Lantern Lane, Brookvale</span></div></div>

  <div class="art" role="img" aria-label="Street map of the office location with a red pin" style="left:75px;top:299px;width:332px;height:181px;background:linear-gradient(135deg,#e6efe0,#f2efe6 45%,#e4ecdc)"></div>

  <svg class="footer-arc" style="top:502px" width="480" height="123" viewBox="0 0 481 119" preserveAspectRatio="none"><path d="M0 40Q240 -20 481 40V119H0Z" fill="#efeff2"/></svg>
  <div class="brand" style="left:69px;top:518px"><i></i>Hearthline</div>
  <p class="fcol" style="left:68px;top:537px;width:85px;color:var(--ink)">Be the first to find out about exclusive deals, the latest Lookbooks trends. We're on a mission to build a better future where technology.</p>
  <div class="social" style="left:68px;top:573px"><i></i><i></i><i></i><i></i></div>
  <div class="fcol" style="left:156px;top:517px"><b>Address</b>Phone: &nbsp;+1 555 014 2290<br>Email: &nbsp;hello@hearthline.co<br>Address: &nbsp;Maple Hollow, Ridgefield,<br>United States</div>
  <div class="fcol" style="left:245px;top:517px"><b>Quick Links</b>Privacy Policy &nbsp; About Us<br>Contact Us</div>
  <div class="fcol" style="left:334px;top:517px;width:85px"><b>Twitter</b>&#9679; Lorem ipsum dolor sit amet, con sectetur adipiscing elit, sed do eius mod tempor incididunt. 2<br>@hearthline</div>
  <div class="dots" style="left:334px;top:563px"><i></i><i></i></div>
  <p class="copy" style="left:68px;top:610px">&copy; 2020, Hearthline | <u>Privacy Policy</u> | <u>Site Map</u></p>
  <p class="copy" style="left:378px;top:610px">All Right Reserved</p>
  <span class="deco" style="left:427px;top:605px">&#10006;</span>
</section>

</body>
</html>
```